Brantley Studios photography and video creator

I need a business card for my production company. I shoot photography and videography for real estate, adventure sports and businesses

Contact Information for Business Card

simple not to busy

Colors

Designer to choose colors to be used in the design.

Requirements
Must have
• derek@brantleystudios.ca
• phone -5873304127
• instagram derek_brantley

```html
<!DOCTYPE html>
<html lang="en">
<head>
<meta charset="UTF-8">
<title>Brantley Studios — Business Card</title>
<link href="https://fonts.googleapis.com/css2?family=Montserrat:wght@400;500;600;700&display=swap" rel="stylesheet">
<style>
  :root {
    --page-bg: #e4e4e4;
    --card-white: #ffffff;
    --ink: #1c1c1c;
    --ink-soft: #707070;
    --scene-light: #e2e2e2;
    --scene-mid: #8a8a8a;
    --scene-dark: #262626;
    --scene-deep: #161616;
    --logo-white: #ffffff;
  }
  * { box-sizing: border-box; margin: 0; padding: 0; }
  html, body {
    width: 1200px; height: 1100px; overflow: hidden;
    background: var(--page-bg);
    font-family: "Montserrat", sans-serif;
  }
  .canvas { position: relative; width: 1200px; height: 1100px; }

  .card {
    position: absolute; left: 221px; width: 757px; height: 442px;
    border-radius: 28px; overflow: hidden;
  }
  .card--front { top: 77px; }
  .card--back { top: 563px; background: var(--card-white); }

  .front-scene {
    position: absolute; inset: 0;
    background: linear-gradient(180deg, var(--scene-light) 0%, var(--scene-mid) 35%, var(--scene-dark) 62%, var(--scene-deep) 100%);
  }
  .front-brand {
    position: absolute; left: 0; right: 0; top: 283px;
    text-align: center; color: var(--logo-white); font-weight: 600;
  }
  .front-brand__name { font-size: 72px; line-height: 1; letter-spacing: 1px; }
  .front-brand__sub { font-size: 19px; letter-spacing: 7px; margin-top: 16px; padding-left: 7px; }

  .badge {
    position: absolute; left: 513px; top: 41px; width: 196px; height: 196px;
    border-radius: 50%;
    background: linear-gradient(180deg, var(--scene-light) 0%, var(--scene-mid) 38%, var(--scene-dark) 62%, var(--scene-deep) 100%);
  }
  .badge__name {
    position: absolute; left: 0; right: 0; top: 117px; text-align: center;
    color: var(--logo-white); font-weight: 600; font-size: 24px; line-height: 1;
  }

  .person { position: absolute; left: 49px; top: 205px; }
  .person__name { font-size: 29px; font-weight: 600; color: var(--ink); line-height: 1.1; }
  .person__first { color: var(--ink-soft); }
  .person__role { font-size: 19px; font-weight: 500; color: var(--ink); margin-top: 4px; }

  .divider {
    position: absolute; left: 49px; top: 274px; width: 660px; height: 2px;
    background: var(--ink);
  }

  .contacts { position: absolute; left: 49px; top: 316px; list-style: none; }
  .contacts__item {
    display: flex; align-items: center; gap: 9px; height: 26px;
    font-size: 19px; color: var(--ink); font-weight: 400;
  }
  .contacts__icon { width: 17px; height: 17px; flex: none; }
</style>
</head>
<body>
<main class="canvas">

  <section class="card card--front">
    <div class="front-scene" role="img" aria-label="Layered grey mountain range with evergreen trees, fading from pale sky to dark foreground"></div>
    <div class="front-brand">
      <div class="front-brand__name">BRANTLEY</div>
      <div class="front-brand__sub">STUDIOS</div>
    </div>
  </section>

  <section class="card card--back">
    <div class="badge" role="img" aria-label="Round emblem with a small mountain and evergreen landscape">
      <div class="badge__name">BRANTLEY</div>
    </div>

    <div class="person">
      <div class="person__name"><span class="person__first">Owen</span> Hale</div>
      <div class="person__role">Manager</div>
    </div>

    <div class="divider"></div>

    <ul class="contacts">
      <li class="contacts__item">
        <svg class="contacts__icon" viewBox="0 0 24 24" aria-hidden="true"><path fill="#555" d="M6.6 10.8a15.1 15.1 0 0 0 6.6 6.6l2.2-2.2c.3-.3.7-.4 1-.2 1.1.4 2.3.6 3.6.6.6 0 1 .4 1 1V20c0 .6-.4 1-1 1A17 17 0 0 1 3 4c0-.6.4-1 1-1h3.5c.6 0 1 .4 1 1 0 1.3.2 2.5.6 3.6.1.3 0 .7-.2 1z"/></svg>
        <span>5873304127</span>
      </li>
      <li class="contacts__item">
        <svg class="contacts__icon" viewBox="0 0 24 24" aria-hidden="true"><circle cx="12" cy="12" r="8.5" fill="none" stroke="#555" stroke-width="2"/></svg>
        <span>derek_brantley</span>
      </li>
      <li class="contacts__item">
        <svg class="contacts__icon" viewBox="0 0 24 24" aria-hidden="true"><rect x="2" y="5" width="20" height="14" fill="#555"/><path d="M2 5l10 8 10-8" fill="none" stroke="#fff" stroke-width="1.8"/></svg>
        <span>derek@brantleystudios.ca</span>
      </li>
    </ul>
  </section>

</main>
</body>
</html>
```